TORVEL Industrial Maintenance

I offer repair and maintenance services of industrial mechanics in Quebec. I would like a creation that reflects confidence, competence, professionalism and dynamism. I like the orange color and the blue color.

Target Market(s)

Industries and Manufacturing companies using industrial machinery for the manufacture of their products.

Industry/Entity Type

Manufacturing

Contact Information for Business Card

TORVEL Maintenance Industrielle
Tél: (450)-318-5947
Courriel: torvel.mnt@boitemel-exemple.com

Font styles to use
Sans Serif

Colors
f78f20
0455a3

Requirements
Must have
• My company name: TORVEL Maintenance Industrielle My phone: (450) -318-5947 My email: torvel.mnt@boitemel-exemple.com
Nice to have
• Integrate a representative logo of the mechanics (gears, mechanical parts)

```html
<!DOCTYPE html>
<html lang="fr">
<head>
<meta charset="utf-8">
<title>TORVEL Maintenance Industrielle – Carte d'affaires</title>
<link rel="stylesheet" href="https://fonts.googleapis.com/css2?family=Cinzel:wght@700&family=Poppins:wght@400;600;700&display=swap">
<style>
  :root {
    --orange: #f78f20;
    --blue: #0455a3;
    --ink: #1d1d1f;
    --white: #ffffff;
    --mist: #ececec;
    --stage: #d9d9d9;
  }
  * { box-sizing: border-box; margin: 0; padding: 0; }
  html, body {
    width: 1200px; height: 933px; overflow: hidden;
    background: var(--stage);
    font-family: "Poppins", sans-serif;
  }
  .canvas { position: relative; width: 1200px; height: 933px; }
  .card {
    position: absolute; width: 620px; height: 354px;
    border-radius: 4px; overflow: hidden;
    box-shadow: 0 10px 30px rgba(0,0,0,0.18);
  }
  .card--back { left: 70px; top: 70px; background: var(--orange); }
  .card--front { left: 510px; top: 500px; background: var(--white); }

  .brand {
    position: absolute; display: flex; align-items: center; gap: 12px;
    font-family: "Poppins", sans-serif; font-weight: 700; letter-spacing: 2px;
  }
  .brand__dot { border-radius: 50%; flex: none; }
  .card--back .brand {
    left: 50%; top: 50%; transform: translate(-50%, -50%);
    color: var(--white); font-size: 54px;
  }
  .card--back .brand__dot { width: 22px; height: 22px; background: var(--white); }
  .card--front .brand {
    left: 44px; top: 150px; color: var(--blue); font-size: 40px;
  }
  .card--front .brand__dot { width: 16px; height: 16px; background: var(--blue); }

  .waves { position: absolute; inset: 0; }

  .identity { position: absolute; right: 40px; top: 36px; text-align: right; }
  .identity__name {
    font-family: "Cinzel", serif; font-weight: 700; font-size: 23px;
    color: var(--ink); letter-spacing: 1px;
  }
  .identity__role {
    font-size: 12px; color: var(--orange); margin-top: 2px;
  }
  .identity__rule {
    width: 130px; height: 1.5px; background: var(--orange);
    margin: 8px 0 0 auto;
  }

  .contact {
    position: absolute; right: 28px; bottom: 24px; text-align: right;
    color: var(--white); font-size: 13px; line-height: 1.7;
  }
  .contact__label { font-weight: 700; }
</style>
</head>
<body>
<main class="canvas">
  <section class="card card--back" aria-label="Verso de la carte">
    <div class="brand"><span class="brand__dot"></span>TORVEL</div>
  </section>

  <section class="card card--front" aria-label="Recto de la carte">
    <svg class="waves" viewBox="0 0 620 354" width="620" height="354" aria-hidden="true">
      <path d="M0,250 C190,256 370,236 460,182 C520,146 575,132 620,128" fill="none" stroke="var(--mist)" stroke-width="6"/>
      <path d="M0,260 C200,266 380,246 470,192 C530,156 580,144 620,140 L620,354 L0,354 Z" fill="var(--orange)"/>
      <path d="M0,278 C210,284 400,262 490,208 C545,174 590,162 620,158 L620,354 L0,354 Z" fill="var(--blue)"/>
    </svg>

    <div class="brand"><span class="brand__dot"></span>TORVEL</div>

    <div class="identity">
      <p class="identity__name">ÉTIENNE TORVEL</p>
      <p class="identity__role">Électromécanicien</p>
      <div class="identity__rule"></div>
    </div>

    <div class="contact">
      <p><span class="contact__label">Tél:</span> (450)-318-5947</p>
      <p><span class="contact__label">Courriel:</span> torvel.mnt@boitemel-exemple.com</p>
      <p>Quebec, Canada</p>
    </div>
  </section>
</main>
</body>
</html>
```